Verpackungsdesign für Lifestyle-Diagnostik und Supplements im Bereich Longevity
Zielgruppe
Wir machen Lifestyle-Diagnostik und Supplements im Bereich Longevity
Aufgabenstellung
Verpackung eines Tests (wie der hier: https://shop.quelmarotix.example/products/tandrix) in der gezeigten Metallschachtel, Supplements in den gezeigten Dosen. Ein Set besteht aus einem Test und zwei Dosen (morgens und abends). Farbschema und Logo Korunelle wie im Anhang. paar Details zu den Supplements auch in den Dateien
Bitte auch an Prägung und anderen Gestaltungsmöglichkeiten denken

```html
<!DOCTYPE html>
<html lang="de">
<head>
<meta charset="utf-8">
<title>Korunelle – Day &amp; Night Complex Etiketten</title>
<link rel="stylesheet" href="https://fonts.googleapis.com/css2?family=Encode+Sans+Semi+Condensed:wght@300;400;600;700&family=Arimo:wght@700&display=swap">
<style>
  :root {
    --lime: #9bc31c;
    --teal-dark: #1d4a50;
    --teal: #0d6e78;
    --ink: #22343a;
    --paper: #ffffff;
    --bg: #ffffff;
    --rule: #333333;
    --silver-light: #e4e6e8;
    --silver-dark: #8d9296;
  }
  * { box-sizing: border-box; margin: 0; padding: 0; }
  html, body { width: 1200px; height: 982px; overflow: hidden; background: var(--bg); }
  body { position: relative; font-family: "Encode Sans Semi Condensed", sans-serif; color: var(--ink); }

  .divider-v { position: absolute; left: 586px; top: 0; width: 1px; height: 982px; background: var(--rule); }
  .divider-h { position: absolute; left: 0; top: 491px; width: 1200px; height: 1px; background: var(--rule); }

  .variant-number { position: absolute; font-family: "Arimo", sans-serif; font-weight: 700; font-size: 44px; color: #1a1a1a; line-height: 1; }

  .lid-view { position: absolute; left: 587px; top: 0; width: 613px; height: 491px; overflow: hidden;
    background: linear-gradient(160deg, #eceef0, #b9bdc1); }
  .lid-disc { position: absolute; left: -40px; top: 20px; width: 720px; height: 560px; border-radius: 50%;
    background: radial-gradient(ellipse at 55% 35%, var(--silver-light), #a9aeb2 60%, var(--silver-dark)); }

  .label { position: absolute; width: 167px; height: 304px; background: var(--paper); border: 1px solid #e3e3e3; overflow: hidden; }
  .brand { position: absolute; left: 15px; top: 48px; display: flex; align-items: center; gap: 6px; }
  .brand-dot { width: 14px; height: 14px; border-radius: 50%; background: var(--lime); }
  .brand-name { font-weight: 600; font-size: 17px; color: var(--lime); }
  .tagline { position: absolute; left: 15px; top: 76px; font-size: 9.5px; font-weight: 400; color: var(--ink); }
  .product-title { position: absolute; left: 15px; top: 108px; font-size: 21px; font-weight: 600; color: var(--lime); }
  .product-icon { position: absolute; left: 15px; top: 140px; width: 26px; height: 32px; }
  .benefits { position: absolute; left: 15px; top: 185px; list-style: none; font-size: 7.5px; line-height: 11px; font-weight: 300; }
  .label-band { position: absolute; left: 0; top: 250px; width: 167px; height: 24px; }

  .label--accent .benefits { left: 22px; top: 188px; }
  .accent-line { position: absolute; left: 14px; top: 174px; width: 2px; height: 82px; }

  .label--color { width: 168px; height: 300px; border: none; }
  .label--day { background: linear-gradient(135deg, #7da51f 0%, #2f6a3c 45%, var(--teal-dark) 70%, var(--teal) 100%); }
  .label--night { background: linear-gradient(135deg, #0f6f78 0%, var(--teal-dark) 40%, #3f7a30 75%, #86ad24 100%); }
  .label--color .brand { left: 0; right: 0; top: 30px; flex-direction: column; gap: 10px; }
  .label--color .brand-dot { width: 22px; height: 22px; background: #ffffff; }
  .label--color .brand-name { font-size: 22px; color: #ffffff; }
  .color-title { position: absolute; left: 22px; top: 122px; font-size: 20px; font-weight: 600; line-height: 24px; color: #ffffff; }
  .color-number { position: absolute; left: 20px; top: 192px; font-size: 56px; font-weight: 300; color: #ffffff; line-height: 1; }
  .graphic-area { position: absolute; left: 70px; top: 175px; width: 88px; height: 110px; border-radius: 4px;
    background: linear-gradient(160deg, rgba(155,195,28,0.35), rgba(155,195,28,0.08)); }
  .side-text { position: absolute; right: 3px; top: 20px; writing-mode: vertical-rl; font-size: 6px; letter-spacing: 1px; color: #ffffff; }
</style>
</head>
<body>
  <svg width="0" height="0" style="position:absolute">
    <defs>
      <linearGradient id="silverBand" x1="0" x2="1"><stop offset="0" stop-color="#c8c9cc"/><stop offset=".5" stop-color="#f2f2f2"/><stop offset="1" stop-color="#b9babd"/></linearGradient>
      <clipPath id="moonOuter"><circle cx="12" cy="17" r="12"/></clipPath>
      <mask id="moonCut"><rect width="26" height="32" fill="#fff"/><circle cx="19" cy="11" r="9" fill="#000"/></mask>
    </defs>
  </svg>

  <!-- Variante 1 -->
  <section class="variant variant-1">
    <div class="label" style="left:73px; top:121px;">
      <div class="brand"><span class="brand-dot"></span><span class="brand-name">Korunelle</span></div>
      <p class="tagline">Täglicher Baustein Zukunft</p>
      <h2 class="product-title">Night-Complex</h2>
      <svg class="product-icon" viewBox="0 0 26 32"><g fill="none" stroke="var(--teal-dark)" stroke-width="2.2"><circle cx="12" cy="17" r="11" mask="url(#moonCut)"/><circle cx="19" cy="11" r="9" clip-path="url(#moonOuter)"/></g></svg>
      <ul class="benefits"><li>Wissenschaftlich fundiert</li><li>Hochreine Wirkstoffe</li><li>Maximale Bioverfügbarkeit</li><li>Laborgeprüfte Qualität</li><li>Made in Germany</li><li>100% Vegan &amp; Ohne Zusatzstoffe</li></ul>
      <svg class="label-band" viewBox="0 0 167 24" preserveAspectRatio="none"><path d="M0 6 Q84 18 167 2 L167 8 Q84 24 0 12 Z" fill="url(#silverBand)"/></svg>
    </div>
    <div class="label" style="left:345px; top:121px;">
      <div class="brand"><span class="brand-dot"></span><span class="brand-name">Korunelle</span></div>
      <p class="tagline">Täglicher Baustein Zukunft</p>
      <h2 class="product-title">Day-Complex</h2>
      <svg class="product-icon" viewBox="0 0 26 32"><g stroke="var(--teal-dark)" stroke-width="2" fill="none" stroke-linecap="round"><circle cx="13" cy="16" r="5"/><path d="M13 3v3M13 26v3M0 16h3M23 16h3M4 7l2 2M20 23l2 2M4 25l2-2M20 9l2-2"/></g></svg>
      <ul class="benefits"><li>Wissenschaftlich fundiert</li><li>Hochreine Wirkstoffe</li><li>Maximale Bioverfügbarkeit</li><li>Laborgeprüfte Qualität</li><li>Made in Germany</li><li>100% Vegan &amp; Ohne Zusatzstoffe</li></ul>
      <svg class="label-band" viewBox="0 0 167 24" preserveAspectRatio="none"><path d="M0 6 Q84 18 167 2 L167 8 Q84 24 0 12 Z" fill="url(#silverBand)"/></svg>
    </div>
    <span class="variant-number" style="left:20px; top:425px;">1</span>
  </section>

  <!-- Deckelprägung -->
  <div class="lid-view" role="img" aria-label="Nahaufnahme des gebürsteten Metalldeckels mit geprägtem Markenzeichen">
    <div class="lid-disc"></div>
  </div>

  <!-- Variante 2 -->
  <section class="variant variant-2">
    <div class="label label--accent" style="left:73px; top:612px;">
      <div class="brand"><span class="brand-dot"></span><span class="brand-name">Korunelle</span></div>
      <p class="tagline">Täglicher Baustein Zukunft</p>
      <h2 class="product-title">Night-Complex</h2>
      <svg class="product-icon" viewBox="0 0 26 32"><g fill="none" stroke="var(--teal-dark)" stroke-width="2.2"><circle cx="12" cy="17" r="11" mask="url(#moonCut)"/><circle cx="19" cy="11" r="9" clip-path="url(#moonOuter)"/></g></svg>
      <span class="accent-line" style="background:var(--teal-dark);"></span>
      <ul class="benefits"><li>Wissenschaftlich fundiert</li><li>Hochreine Wirkstoffe</li><li>Maximale Bioverfügbarkeit</li><li>Laborgeprüfte Qualität</li><li>Made in Germany</li><li>100% Vegan &amp; Ohne Zusatzstoffe</li></ul>
      <svg class="label-band" viewBox="0 0 167 24" preserveAspectRatio="none"><path d="M0 6 Q84 18 167 2 L167 8 Q84 24 0 12 Z" fill="var(--teal-dark)"/></svg>
    </div>
    <div class="label label--accent" style="left:345px; top:612px;">
      <div class="brand"><span class="brand-dot"></span><span class="brand-name">Korunelle</span></div>
      <p class="tagline">Täglicher Baustein Zukunft</p>
      <h2 class="product-title">Day-Complex</h2>
      <svg class="product-icon" viewBox="0 0 26 32"><g stroke="var(--teal-dark)" stroke-width="2" fill="none" stroke-linecap="round"><circle cx="13" cy="16" r="5"/><path d="M13 3v3M13 26v3M0 16h3M23 16h3M4 7l2 2M20 23l2 2M4 25l2-2M20 9l2-2"/></g></svg>
      <span class="accent-line" style="background:var(--lime);"></span>
      <ul class="benefits"><li>Wissenschaftlich fundiert</li><li>Hochreine Wirkstoffe</li><li>Maximale Bioverfügbarkeit</li><li>Laborgeprüfte Qualität</li><li>Made in Germany</li><li>100% Vegan &amp; Ohne Zusatzstoffe</li></ul>
      <svg class="label-band" viewBox="0 0 167 24" preserveAspectRatio="none"><path d="M0 6 Q84 18 167 2 L167 8 Q84 24 0 12 Z" fill="var(--lime)"/></svg>
    </div>
    <span class="variant-number" style="left:20px; top:918px;">2</span>
  </section>

  <!-- Variante 3 -->
  <section class="variant variant-3">
    <div class="label label--color label--day" style="left:658px; top:611px;">
      <div class="brand"><span class="brand-dot"></span><span class="brand-name">Korunelle</span></div>
      <h2 class="color-title">Day<br>Complex</h2>
      <div class="graphic-area" role="img" aria-label="Dekorative Streifengrafik in Limettengrün"></div>
      <span class="color-number">1</span>
      <span class="side-text">Longevity Supplement Kapseln</span>
    </div>
    <div class="label label--color label--night" style="left:958px; top:611px;">
      <div class="brand"><span class="brand-dot"></span><span class="brand-name">Korunelle</span></div>
      <h2 class="color-title">Night<br>Complex</h2>
      <div class="graphic-area" role="img" aria-label="Dekorative Streifengrafik in Limettengrün"></div>
      <span class="color-number">2</span>
      <span class="side-text">Longevity Supplement Kapseln</span>
    </div>
    <span class="variant-number" style="left:608px; top:918px;">3</span>
  </section>

  <div class="divider-v"></div>
  <div class="divider-h"></div>
</body>
</html>
```